Mortgage firm needs clean and simple wordpress website and logo

The competition is for design only, and the winning design for the homepage will be expected to create a second design for a simpler template for additional pages.

We need a logo and basic wordpress website design for a Sydney based mortgage firm.
We need a clean and simple logo and website, based on the mortgage/accounting/finance/tax industry. Simple, credible and official colors.

The logo is expected to be so simple that we have combined into the one job.
If you submit a logo design and we choose it along with someone else's website design you will be paid a bonus of $60. The website design will still win the competition as per normal.

Current website is old and terrible but gives you an idea of the sitemap (super simple) and what they do: http://www.lendbridgeloans.com.au/

We will integrate a mortgage calculator into the site.
The calculator is adjustable in styles, you can see it here: http://www.lendbridgeloans.com.au/mortgagecalculator/

We want original different to copy-and-paste template looking designs.
We like simple websites with a long home page and a few additional pages like https://www.homefundpath.com.au/

We are based in Sydney Australia and are mortgage brokers

We want a clean, formal, credible site, limited pages.

The project is guaranteed, so go for it.

Example of basic template after home page complete: http://lendbridgeloans.com.au/template_example.jpg

Target Market(s)

Mortgage and banking clients

Industry/Entity Type

Finance

Number of Pages Required

1 page

Requirements
Must have
• A simple logo, Wordpress capable, be able to incorporate the mortgage calculator (on the home page if needed as well as its own page)
Nice to have
• VIdeo - something free but nice

```html
<!DOCTYPE html>
<html lang="en">
<head>
<meta charset="utf-8">
<title>Lendbridge Loans – Private Funding</title>
<link href="https://fonts.googleapis.com/css2?family=Nunito+Sans:wght@300;400;600;700;800&display=swap" rel="stylesheet">
<style>
:root{
  --blue:#1170ae;
  --blue-dark:#0d5f95;
  --orange:#f26a21;
  --sand:#f0eeec;
  --ink:#1d1d1d;
  --muted:#6b6b6b;
  --line:#dedede;
  --white:#ffffff;
}
*{box-sizing:border-box;margin:0;padding:0}
html,body{width:1200px;height:2490px;overflow:hidden}
body{position:relative;background:var(--white);font-family:"Nunito Sans",Arial,sans-serif;color:var(--ink)}
.abs{position:absolute}
.caps{text-transform:uppercase;letter-spacing:.08em}

/* hero */
.hero{left:0;top:0;width:1200px;height:598px;background:linear-gradient(100deg,#f3f1ef 0%,#e6e2dd 35%,#8a8e97 60%,#3e4658 80%,#5b6272 100%)}
.hero-fade{left:0;top:0;width:700px;height:598px;background:linear-gradient(90deg,rgba(246,244,242,.92) 0%,rgba(246,244,242,.7) 70%,rgba(246,244,242,0) 100%)}
.brand{left:156px;top:33px;display:flex;align-items:center;gap:10px}
.brand-square{width:60px;height:60px;border:4px solid var(--blue)}
.brand-name{font-weight:800;font-size:15px;line-height:1.15;color:var(--ink);letter-spacing:.04em}
.nav-top-bar{left:463px;top:0;width:85px;height:5px;background:var(--orange)}
.nav a{position:absolute;top:66px;font-size:12px;font-weight:700;color:var(--ink);text-decoration:none;letter-spacing:.06em}
.nav a.current{color:var(--orange)}
.phone-btn{left:1003px;top:59px;width:30px;height:30px;border-radius:50%;background:var(--blue);display:flex;align-items:center;justify-content:center}
.hero-title{left:156px;top:258px;font-size:24px;font-weight:800;color:var(--blue)}
.hero-sub{left:156px;top:290px;font-size:20px;font-weight:600}
.hero-copy{left:156px;top:328px;width:490px;font-size:15px;line-height:1.45;color:#444}
.btn-outline{display:flex;align-items:center;justify-content:center;font-size:11px;font-weight:800;letter-spacing:.1em;color:var(--ink);border:2px solid var(--blue);background:transparent}
.hero-btn{left:156px;top:395px;width:143px;height:33px}

/* intro */
.intro{left:0;top:598px;width:1200px;height:469px;background:var(--sand)}
.intro-mark{left:568px;top:647px;width:64px;height:64px;border:4px solid var(--blue)}
.intro-title{left:0;top:728px;width:1200px;text-align:center;font-size:20px;font-weight:700}
.intro-copy{left:310px;top:757px;width:580px;text-align:center;font-size:12.5px;line-height:1.6;color:#444}
.intro-link{left:0;top:830px;width:1200px;text-align:center;font-size:11px;font-weight:800;color:var(--blue);letter-spacing:.1em}

/* calculator */
.calc{left:232px;top:891px;width:736px;height:586px;background:var(--white);box-shadow:0 6px 24px rgba(0,0,0,.08)}
.calc-head{left:232px;top:891px;width:736px;height:176px;background:var(--blue)}
.calc-title{left:232px;top:930px;width:736px;text-align:center;font-size:28px;font-weight:700;color:var(--white)}
.field-label{font-size:13px;font-weight:600;color:var(--white)}
.field{display:flex;height:30px}
.field .val{flex:1;background:var(--white);font-size:12px;color:#999;padding:7px 10px}
.field .unit{width:44px;background:var(--orange);color:var(--white);font-size:10px;font-weight:800;display:flex;align-items:center;justify-content:center;letter-spacing:.06em}
.calc-result{left:232px;top:1094px;width:736px;text-align:center;font-size:14px;font-weight:700;letter-spacing:.05em}
.stat-label{font-size:12px;font-weight:600;color:#444}
.stat-value{font-size:21px;color:#666}
.select-label{font-size:13px;font-weight:600;color:#333}
.select{display:flex;height:30px;border:1px solid var(--line)}
.select .txt{flex:1;font-size:11px;color:#777;padding:7px 10px}
.select .arrow{width:30px;background:var(--blue);display:flex;align-items:center;justify-content:center}
.btn-solid{background:var(--orange);color:var(--white);font-size:10px;font-weight:800;letter-spacing:.06em;display:flex;align-items:center;justify-content:center}

/* why us */
.why-title{left:0;top:1535px;width:1200px;text-align:center;font-size:20px;font-weight:700}
.why-card{top:1589px;width:241px;height:239px;background:var(--sand);text-align:center}
.why-icon{position:absolute;left:90px;top:40px}
.why-name{position:absolute;left:0;top:128px;width:100%;font-size:15px;font-weight:800;letter-spacing:.05em}
.why-text{position:absolute;left:22px;top:148px;width:197px;font-size:12px;line-height:1.4;color:#333}

/* cta */
.cta{left:0;top:1876px;width:1200px;height:119px;background:var(--orange)}
.cta-text{left:232px;top:1914px;font-size:28px;font-weight:300;color:var(--white)}
.cta-text strong{font-weight:800}
.cta-btn{left:823px;top:1919px;width:145px;height:33px;border:2px solid var(--white);color:var(--white);font-size:11px;font-weight:800;letter-spacing:.1em;display:flex;align-items:center;justify-content:center}

/* newsletter */
.news-label{left:232px;top:2038px;font-size:14px;font-weight:700}
.news-rule{left:232px;top:2068px;width:50px;height:2px;background:var(--ink)}
.news-field{top:2040px;height:30px;border-bottom:1px solid var(--line);font-size:11px;font-style:italic;color:#aaa;padding-left:14px}

/* contact */
.contact{left:232px;top:2118px;width:736px;height:266px;background:var(--sand)}
.contact-title{left:232px;top:2160px;width:736px;text-align:center;font-size:11px;font-weight:800;letter-spacing:.1em}
.person{top:2200px;width:200px;text-align:center}
.person .name{font-size:15px;color:#555}
.person .tel{font-size:11px;color:#333;font-weight:600}
.main-call{left:450px;top:2198px;width:300px;text-align:center}
.main-call .call{font-size:20px;font-weight:700;color:var(--blue)}
.main-call .fax{font-size:11px;color:#666}
.contact-rule{top:2284px;height:1px;background:#cfcccb}
.address{left:232px;top:2322px;width:736px;text-align:center;font-size:12px;color:#666}

/* footer */
.copyright{left:232px;top:2428px;font-size:11px;color:#888}
.social{left:790px;top:2428px;display:flex;align-items:center;gap:7px;font-size:11px;color:#999}
.social .dot{width:8px;height:8px;border-radius:50%;background:#999}
.social .dot.active{background:var(--orange)}
</style>
</head>
<body>

<!-- hero -->
<div class="abs hero" role="img" aria-label="Photo of two smiling businessmen in suits reviewing a tablet at a desk"></div>
<div class="abs hero-fade"></div>
<div class="abs nav-top-bar"></div>
<div class="abs brand">
  <div class="brand-square"></div>
  <div class="brand-name">LENDBRIDGE<br>LOANS</div>
</div>
<nav class="nav">
  <a class="current" style="left:486px" href="#">HOME</a>
  <a style="left:569px" href="#">ABOUT US</a>
  <a style="left:680px" href="#">MORTGAGE CALCULATOR</a>
  <a style="left:888px" href="#">CONTACT US</a>
</nav>
<div class="abs phone-btn">
  <svg width="16" height="16" viewBox="0 0 16 16"><path d="M2 9 C2 5 14 5 14 9 L11.5 10.5 L10.5 8.5 C9 8 7 8 5.5 8.5 L4.5 10.5 Z" fill="#fff"/></svg>
</div>
<h1 class="abs hero-title">LENDBRIDGE LOANS</h1>
<div class="abs hero-sub">Private Funding</div>
<p class="abs hero-copy">Home, investment and commercial loans for purchase, refinance and consolidation at up to 80% lending.</p>
<div class="abs btn-outline hero-btn">CONTACT US</div>

<!-- intro -->
<div class="abs intro"></div>
<div class="abs intro-mark"></div>
<h2 class="abs intro-title">We have arranged finance for clients</h2>
<p class="abs intro-copy">over many years through banks, non-bank lenders, mortgage managers and brokers. With a lending panel that includes the major banks through to more exclusive lenders ...</p>
<div class="abs intro-link">ABOUT US &#8594;</div>

<!-- calculator -->
<div class="abs calc"></div>
<div class="abs calc-head"></div>
<h2 class="abs calc-title">Mortgage Calculator</h2>

<div class="abs field-label" style="left:307px;top:987px">Loan Amount</div>
<div class="abs field" style="left:307px;top:1012px;width:163px"><div class="val">$ &nbsp;100000</div><div class="unit">AUD</div></div>
<div class="abs field-label" style="left:508px;top:987px">Loan Term</div>
<div class="abs field" style="left:508px;top:1012px;width:184px"><div class="val">30</div><div class="unit" style="width:64px">YEARS</div></div>
<div class="abs field-label" style="left:709px;top:987px">Loan Interest</div>
<div class="abs field" style="left:709px;top:1012px;width:182px"><div class="val">06</div><div class="unit" style="width:64px">%</div></div>

<div class="abs calc-result">YOUR REPAYMENT WOULD BE 600 PER MONTH</div>

<svg class="abs" style="left:340px;top:1140px" width="400" height="230" viewBox="340 1140 400 230">
  <g stroke="#e4e4e4" stroke-width="1">
    <line x1="435" y1="1157" x2="717" y2="1157"/>
    <line x1="435" y1="1198" x2="717" y2="1198"/>
    <line x1="435" y1="1239" x2="717" y2="1239"/>
    <line x1="435" y1="1279" x2="717" y2="1279"/>
    <line x1="435" y1="1320" x2="717" y2="1320"/>
    <line x1="435" y1="1150" x2="435" y2="1325"/>
  </g>
  <g font-family="Nunito Sans, Arial, sans-serif" font-size="11" fill="#777" text-anchor="end">
    <text x="405" y="1161">100,000</text>
    <text x="405" y="1202">75,000</text>
    <text x="405" y="1243">50,000</text>
    <text x="405" y="1283">25,000</text>
    <text x="405" y="1324">0</text>
  </g>
  <g font-family="Nunito Sans, Arial, sans-serif" font-size="11" fill="#777" text-anchor="middle">
    <text x="485" y="1354">2020</text>
    <text x="581" y="1354">2030</text>
    <text x="667" y="1354">2040</text>
  </g>
  <path d="M435 1157 C470 1160 500 1172 529 1184 C560 1198 595 1215 623 1233 C650 1250 680 1268 700 1295 C708 1305 713 1313 717 1320" fill="none" stroke="#f26a21" stroke-width="2"/>
  <g fill="#f26a21">
    <circle cx="435" cy="1157" r="3"/><circle cx="459" cy="1160" r="3"/><circle cx="482" cy="1168" r="3"/>
    <circle cx="506" cy="1175" r="3"/><circle cx="529" cy="1184" r="3"/><circle cx="553" cy="1194" r="3"/>
    <circle cx="576" cy="1205" r="3"/><circle cx="600" cy="1218" r="3"/><circle cx="623" cy="1233" r="3"/>
    <circle cx="647" cy="1249" r="3"/><circle cx="670" cy="1268" r="3"/><circle cx="694" cy="1290" r="3"/>
    <circle cx="717" cy="1320" r="3"/>
  </g>
  <rect x="573" y="1182" width="137" height="30" fill="#fff" stroke="#ddd"/>
  <g font-family="Nunito Sans, Arial, sans-serif" font-size="9.5" fill="#444" text-anchor="middle">
    <text x="641" y="1194">Principal Remaining: 53674</text>
    <text x="641" y="1207">Years Remaining: 10</text>
  </g>
</svg>

<div class="abs stat-label" style="left:739px;top:1150px">Repayments</div>
<div class="abs stat-value" style="left:739px;top:1170px">215838</div>
<div class="abs stat-label" style="left:739px;top:1217px">Interest</div>
<div class="abs stat-value" style="left:739px;top:1236px">15838</div>

<div class="abs select-label" style="left:307px;top:1390px">Repayment Type</div>
<div class="abs select" style="left:307px;top:1416px;width:196px"><div class="txt">Principal &amp; Interest</div><div class="arrow"><svg width="10" height="6" viewBox="0 0 10 6"><path d="M1 1 L5 5 L9 1" stroke="#fff" stroke-width="1.8" fill="none"/></svg></div></div>
<div class="abs select-label" style="left:520px;top:1390px">Repayment Frequency</div>
<div class="abs select" style="left:520px;top:1416px;width:195px"><div class="txt">Monthly</div><div class="arrow"><svg width="10" height="6" viewBox="0 0 10 6"><path d="M1 1 L5 5 L9 1" stroke="#fff" stroke-width="1.8" fill="none"/></svg></div></div>
<div class="abs btn-solid" style="left:740px;top:1416px;width:151px;height:30px">CHECK IN ARCHIVE</div>

<!-- why us -->
<h2 class="abs why-title">Why Us?</h2>
<div class="abs why-card" style="left:232px">
  <svg class="why-icon" width="62" height="62" viewBox="0 0 62 62"><circle cx="31" cy="31" r="27" fill="none" stroke="#1170ae" stroke-width="3"/><path d="M31 16 L35 26 L46 26 L37 33 L40 44 L31 37 L22 44 L25 33 L16 26 L27 26 Z" fill="none" stroke="#1170ae" stroke-width="2.5" stroke-linejoin="round"/></svg>
  <div class="why-name">EXPERIENCE</div>
  <div class="why-text">Lendbridge Loans have been organising and managing money for clients for over 25 years.</div>
</div>
<div class="abs why-card" style="left:480px">
  <svg class="why-icon" width="62" height="62" viewBox="0 0 62 62"><circle cx="33" cy="35" r="22" fill="none" stroke="#1170ae" stroke-width="3.5"/><rect x="29" y="6" width="8" height="5" fill="#1170ae"/><line x1="33" y1="35" x2="33" y2="22" stroke="#1170ae" stroke-width="3"/><line x1="33" y1="35" x2="42" y2="35" stroke="#1170ae" stroke-width="3"/><line x1="1" y1="28" x2="9" y2="28" stroke="#1170ae" stroke-width="3"/><line x1="3" y1="36" x2="9" y2="36" stroke="#1170ae" stroke-width="3"/></svg>
  <div class="why-name">FAST</div>
  <div class="why-text">We can provide money in 24 Hours, providing you meet the loan criteria.</div>
</div>
<div class="abs why-card" style="left:727px">
  <svg class="why-icon" width="62" height="62" viewBox="0 0 62 62"><rect x="22" y="6" width="30" height="20" rx="2" fill="#1170ae" transform="rotate(-20 37 16)"/><circle cx="37" cy="17" r="5" fill="#f0eeec"/><path d="M6 40 L24 40 L38 46 L52 40 L56 44 L40 56 L6 56 Z" fill="#1170ae"/></svg>
  <div class="why-name">PRIVATE</div>
  <div class="why-text">Our specialty is private lending for residential, commercial and industrial properties.</div>
</div>

<!-- call to action -->
<div class="abs cta"></div>
<div class="abs cta-text">Talk to a Lendbridge <strong>Loans expert</strong></div>
<div class="abs cta-btn">CONTACT US</div>

<!-- newsletter -->
<div class="abs news-label">Register for our daily updates</div>
<div class="abs news-rule"></div>
<div class="abs news-field" style="left:485px;width:179px">Name</div>
<div class="abs news-field" style="left:686px;width:282px">Email</div>
<svg class="abs" style="left:944px;top:2044px" width="14" height="14" viewBox="0 0 14 14"><path d="M1 7 L13 1 L9 13 L7 8 Z" fill="#1170ae"/></svg>

<!-- contact -->
<div class="abs contact"></div>
<div class="abs contact-title">CONTACT INFO</div>
<div class="abs person" style="left:284px"><div class="name">Daniel R. Whitford</div><div class="tel">+614 2273 4410</div></div>
<div class="abs main-call"><div class="call">Call: +612 9410 5500</div><div class="fax">Fax: +612 9410 5501</div></div>
<div class="abs person" style="left:716px"><div class="name">Steven J. Corrie</div><div class="tel">+614 2273 4488</div></div>
<div class="abs contact-rule" style="left:282px;width:303px"></div>
<div class="abs contact-rule" style="left:615px;width:303px"></div>
<svg class="abs" style="left:590px;top:2272px" width="20" height="24" viewBox="0 0 20 24"><path d="M10 2 C5 2 3 6 3 9 C3 14 10 20 10 20 C10 20 17 14 17 9 C17 6 15 2 10 2 Z" fill="none" stroke="#333" stroke-width="1.6"/><circle cx="10" cy="9" r="2.5" fill="none" stroke="#333" stroke-width="1.6"/><line x1="3" y1="22" x2="17" y2="22" stroke="#333" stroke-width="1.6"/></svg>
<div class="abs address">Suite 12/140 Harbour Rd, Rosehill NSW 2142, Australia</div>

<!-- footer -->
<div class="abs copyright">&#169; 2016 Lendbridge Loans Pty Ltd. ACN 118 274 903</div>
<div class="abs social"><span class="dot"></span>/<span class="dot active"></span>/<span class="dot"></span>/<span class="dot"></span></div>
<svg class="abs" style="left:1008px;top:2418px" width="22" height="32" viewBox="0 0 22 32"><path d="M2 2 L20 2 L20 30 L11 22 L2 30 Z" fill="none" stroke="#f26a21" stroke-width="2.5" stroke-linejoin="round"/></svg>

</body>
</html>
```